Velquora Design
Would like the design to go over the page in a way that can type over it.
We are a personal training and small group studio
Want it to be professional and classy
Updates
Project Deadline Extended
Reason: Asked for some modifications on a few designs, want to give the designers time to do this
Target Market(s)
All age groups, sports professionals as well as business professionals, families
Industry/Entity Type
Training
Requirements
Must have
- Must have Velquora Studio
Mina Tellaver
214 Barnicot Lane
Wexcombe Vale
South Australia 5173
Phone: 0438917263
Nice to have
- Professional classy fonts
Colour
Should not have
- Clip art
Balloons

```html
<!DOCTYPE html>
<html lang="en">
<head>
<meta charset="utf-8">
<title>Velquora Studio Letterhead</title>
<link rel="stylesheet" href="https://fonts.googleapis.com/css2?family=Arimo:wght@400;700&display=swap">
<style>
  :root {
    --brand-blue: #1a8fd6;
    --brand-orange: #f59a2a;
    --text-dark: #1d2a3a;
    --rule-grey: #b9c3cc;
    --paper: #ffffff;
    --wash-blue: #cfe6f5;
    --wash-orange: #fbe0c4;
  }
  * { box-sizing: border-box; margin: 0; padding: 0; }
  html, body {
    width: 870px;
    height: 1200px;
    overflow: hidden;
    background: var(--paper);
  }
  .letterhead {
    position: relative;
    width: 870px;
    height: 1200px;
    background: var(--paper);
    font-family: "Arimo", Arial, sans-serif;
    color: var(--text-dark);
    overflow: hidden;
  }
  .brand {
    position: absolute;
    left: 34px;
    top: 22px;
    display: flex;
    align-items: center;
    gap: 20px;
  }
  .brand-dot {
    width: 74px;
    height: 74px;
    border-radius: 50%;
    background: var(--brand-orange);
  }
  .brand-name {
    font-size: 62px;
    font-weight: 700;
    color: var(--brand-blue);
    letter-spacing: 0.5px;
    line-height: 1;
  }
  .contact {
    position: absolute;
    right: 26px;
    top: 20px;
    text-align: right;
    font-size: 13px;
    line-height: 17px;
  }
  .contact-studio {
    font-size: 22px;
    line-height: 26px;
    font-weight: 700;
    color: var(--brand-blue);
  }
  .contact-person {
    font-size: 19px;
    line-height: 24px;
    font-weight: 700;
    color: var(--text-dark);
    margin-bottom: 3px;
  }
  .header-rule {
    position: absolute;
    left: 18px;
    right: 18px;
    top: 150px;
    border-top: 3px dotted var(--rule-grey);
  }
  .backdrop-mark {
    position: absolute;
    left: 110px;
    top: 175px;
    width: 760px;
    height: 1025px;
    border-radius: 48% 52% 0 0 / 30% 30% 0 0;
    background:
      radial-gradient(circle at 64% 14%, var(--wash-orange) 0, rgba(251,224,196,0) 22%),
      radial-gradient(ellipse at 45% 55%, var(--wash-blue) 0, rgba(207,230,245,0) 65%);
    opacity: 0.55;
  }
</style>
</head>
<body>
  <main class="letterhead">
    <div class="backdrop-mark" role="img" aria-label="Faint background brand figure, soft blue and orange wash"></div>

    <header class="brand">
      <span class="brand-dot"></span>
      <span class="brand-name">Velquora Studio</span>
    </header>

    <address class="contact">
      <div class="contact-studio">Velquora Studio</div>
      <div class="contact-person">Mina Tellaver</div>
      <div>214 Barnicot Lane</div>
      <div>Wexcombe Vale, South Australia 5173</div>
      <div>Phone: 0438917263</div>
    </address>

    <div class="header-rule"></div>
  </main>
</body>
</html>
```